QRV Law Letterhead

Want law firm letterhead - both in terms of a pdf file that I can use electronically as letterhead by adding it as a background - and in terms of a file that I can send to a company to create actual letterhead.
Industry/Entity Type
Law Firm
Font styles to use
Sans Serif
Requirements
Must have
- Should have the following information (you can decide where to place):
- My name - Corwin Haldane
- My email - corwin@qrvlawfirm.example
- My address - 2816 Pellworth Parkway 317-842
- San Jose, California 95742
- Website - www.qrvlawfirm.example
- Phone - 408-555-0187
- Fax - 408-555-0243
- The logo I attached
Nice to have
- I think I would prefer to have a black and white color scheme.
- I don't necessarily need a title after my name, but I have seen a few design submissions that include a generic title. The title I would use is "IP Litigator & Trademark Attorney"

```html
<!DOCTYPE html>
<html lang="en">
<head>
<meta charset="utf-8">
<title>QRV Law Letterhead</title>
<link href="https://fonts.googleapis.com/css2?family=Open+Sans:ital,wght@0,400;0,600;0,700;1,400;1,700&display=swap" rel="stylesheet">
<style>
  :root {
    --backdrop: #e4e5e3;
    --paper: #ffffff;
    --ink: #1e1e20;
    --band-dark: #1f1f22;
    --band-mid: #4a4a4f;
    --band-light: #7b7b80;
    --accent: #44627a;
    --muted: #555a5f;
  }
  * { box-sizing: border-box; margin: 0; padding: 0; }
  html, body { width: 1200px; height: 784px; overflow: hidden; }
  body {
    background: var(--backdrop);
    font-family: "Open Sans", Arial, sans-serif;
    display: flex; align-items: center; justify-content: center;
  }
  .letterhead {
    position: relative;
    width: 572px; height: 740px;
    background: var(--paper);
    box-shadow: 0 2px 10px rgba(0,0,0,0.12);
    overflow: hidden;
  }
  .header-band { position: absolute; top: 0; left: 0; width: 572px; height: 60px; }
  .brand {
    position: absolute; top: 9px; left: 14px;
    display: flex; align-items: center; gap: 6px;
    line-height: 1;
  }
  .brand-mark { width: 10px; height: 10px; border-radius: 50%; background: var(--accent); flex: none; }
  .brand-name { font-size: 23px; font-weight: 600; color: var(--ink); letter-spacing: 0.3px; white-space: nowrap; }
  .signatory {
    position: absolute; top: 40px; left: 186px;
    font-size: 7.5px; line-height: 1; color: var(--ink); font-style: italic; white-space: nowrap;
  }
  .signatory-name { font-weight: 700; color: var(--accent); }
  .contact-footer {
    position: absolute; left: 14px; right: 14px; bottom: 12px;
    display: flex; align-items: center; gap: 6px;
    font-size: 6.8px; line-height: 1; color: var(--muted); font-style: italic; white-space: nowrap;
  }
  .contact-item { display: flex; align-items: center; gap: 3px; }
  .contact-dot { width: 5px; height: 5px; border-radius: 50%; background: var(--accent); flex: none; }
  .footer-rule { position: absolute; left: 0; bottom: 0; width: 100%; height: 5px; background: var(--accent); }
</style>
</head>
<body>
  <main class="letterhead">
    <svg class="header-band" viewBox="0 0 572 60" aria-hidden="true">
      <defs>
        <linearGradient id="band-shade" x1="0" y1="0" x2="1" y2="0">
          <stop offset="0" stop-color="var(--band-dark)"/>
          <stop offset="0.6" stop-color="var(--band-mid)"/>
          <stop offset="1" stop-color="var(--band-light)"/>
        </linearGradient>
      </defs>
      <rect class="top-strip" x="0" y="0" width="175" height="4" fill="var(--band-dark)"/>
      <rect x="0" y="4" width="175" height="1.5" fill="var(--accent)"/>
      <polygon class="band-body" points="168,0 572,0 572,54 372,54 364,40 364,34 190,34 168,26" fill="url(#band-shade)"/>
      <polyline class="band-stripe" points="168,29 189,37 367,37 367,41 375,56 572,56" fill="none" stroke="var(--accent)" stroke-width="2"/>
    </svg>

    <div class="brand">
      <span class="brand-mark"></span>
      <span class="brand-name">QRV Law</span>
    </div>

    <p class="signatory"><span class="signatory-name">Corwin Haldane</span> | IP Litigator &amp; Trademark Attorney</p>

    <footer class="contact-footer">
      <span class="contact-item"><span class="contact-dot"></span>2816 Pellworth Parkway 317-842 San Jose, California 95742</span>
      <span class="contact-item"><span class="contact-dot"></span>408-555-0187</span>
      <span class="contact-item"><span class="contact-dot"></span>408-555-0243</span>
      <span class="contact-item"><span class="contact-dot"></span>corwin@qrvlawfirm.example</span>
      <span class="contact-item"><span class="contact-dot"></span>www.qrvlawfirm.example</span>
    </footer>
    <div class="footer-rule"></div>
  </main>
</body>
</html>
```